Wedding and event Photography company.

We need a business card design for a photography company based in Singapore named LumaVek. Our core service offering is wedding photojournalism. We would like to see minimalistic designs that use the colour white. The final design should communicate a sense of ease and reliability.

The attached are a couple of visual reference which i found over the web, i hope it will helps.

Project Brief Update (14th July 2014):
- Please refrain from using any images from the website for the design. The laws and regulations over here does not allow me to distribute my client's images. Thanks!

Target Market(s)

Young and middle aged adults aged 24 - 38. With money to spend =D

Industry/Entity Type

Business

Contact Information for Business Card

Name: Dax Pell
Designation: Head Photographer
Mobile: +65 84126079
Email: tan@lumavek.example
Website: www.lumavek.example

Font styles to use
Other font styles liked:
• Baskerville URW

Colors

Designer to choose colors to be used in the design.

Requirements
Must have
• Must include:
• - The brand LumaVek
• - The logo attached
• - Please help to place the brand LumaVek with the logo according to your preferences.
• - Services
• - Wedding Photography
• - Portraiture
• - Photojournalism
Nice to have
• Looking forward to an elegant and simple design. Please see attached examples!
• Please use Serif Fonts
Should not have
• Please refrain from using dark tones for the majority of the design.
• Please refrain from letterpress and embossing.

```html
<!DOCTYPE html>
<html lang="en">
<head>
<meta charset="utf-8">
<title>LumaVek — Business Card</title>
<link rel="stylesheet" href="https://fonts.googleapis.com/css2?family=Crimson+Pro:wght@400;700&display=swap">
<style>
  :root {
    --backdrop: #d5d5d5;
    --paper: #e8e7e4;
    --edge-lilac: #c99ad6;
    --ink: #1a1a1a;
    --ink-soft: #4a4a4a;
    --rule: #3a3a3a;
  }
  * { margin: 0; padding: 0; box-sizing: border-box; }
  html, body {
    width: 1200px;
    height: 918px;
    overflow: hidden;
    background: var(--backdrop);
    font-family: "Crimson Pro", "Times New Roman", serif;
    color: var(--ink);
  }
  .canvas {
    position: relative;
    width: 1200px;
    height: 918px;
  }
  .card {
    position: absolute;
    top: 294px;
    width: 540px;
    height: 330px;
    background: var(--paper);
    box-shadow: 0 4px 0 var(--edge-lilac), 0 14px 28px rgba(0,0,0,0.14);
  }
  .card--front { left: 45px; }
  .card--back { left: 615px; }

  .front-stack {
    position: absolute;
    inset: 0;
    display: flex;
    flex-direction: column;
    align-items: center;
    justify-content: center;
    gap: 22px;
  }
  .brand {
    display: flex;
    align-items: center;
    gap: 18px;
  }
  .brand__mark {
    width: 14px;
    height: 14px;
    border-radius: 50%;
    background: var(--ink);
  }
  .brand__name {
    font-size: 58px;
    font-weight: 400;
    line-height: 1;
    letter-spacing: 0.5px;
  }
  .services {
    display: flex;
    gap: 14px;
    list-style: none;
    font-size: 13px;
    letter-spacing: 1.6px;
    text-transform: uppercase;
    color: var(--ink-soft);
  }
  .services li + li::before {
    content: "·";
    margin-right: 14px;
  }

  .corner-mark {
    position: absolute;
    top: 66px;
    right: 52px;
    width: 20px;
    height: 20px;
    border-radius: 50%;
    background: var(--ink);
  }
  .holder {
    position: absolute;
    left: 32px;
    right: 32px;
    top: 150px;
  }
  .holder__heading {
    padding-left: 14px;
    padding-bottom: 12px;
    border-bottom: 1px solid var(--rule);
  }
  .holder__name {
    font-size: 40px;
    font-weight: 400;
    line-height: 1;
  }
  .holder__title {
    margin-top: 8px;
    font-size: 12px;
    letter-spacing: 1.6px;
    text-transform: uppercase;
    color: var(--ink-soft);
  }
  .holder__contacts {
    margin-top: 14px;
    font-size: 11.2px;
    white-space: nowrap;
    letter-spacing: 0.1px;
  }
  .holder__contacts b { font-weight: 700; }
  .holder__contacts .item { margin-right: 5px; }
</style>
</head>
<body>
  <main class="canvas">
    <section class="card card--front" aria-label="Card front">
      <div class="front-stack">
        <div class="brand">
          <span class="brand__mark" aria-hidden="true"></span>
          <span class="brand__name">LumaVek</span>
        </div>
        <ul class="services">
          <li>Wedding Photography</li>
          <li>Portraiture</li>
          <li>Photojournalism</li>
        </ul>
      </div>
    </section>

    <section class="card card--back" aria-label="Card back">
      <span class="corner-mark" aria-hidden="true"></span>
      <div class="holder">
        <div class="holder__heading">
          <h1 class="holder__name">Dax Pell</h1>
          <p class="holder__title">Head Photographer</p>
        </div>
        <p class="holder__contacts">
          <span class="item"><b>P:</b> +65 84126079</span>
          <span class="item"><b>E:</b> tan@lumavek.example</span>
          <span class="item"><b>W:</b> www.lumavek.example</span>| Reg No: 48821067K
        </p>
      </div>
    </section>
  </main>
</body>
</html>
```